Website Redesign - home improvements/garage door supplier & installer in London

We are a garage door specialist providing installation, automation and repair services throughout the South East England with 5 branches/showrooms across London and over 65 employees. Garage doors are our main area of expertise but we have other home improvement products in our range - front/entrance doors, internal doors, sliding and bi-fold patio doors; awnings and shading systems.

Our current website is quite boring and uninviting so we are looking to redesign and modernise the whole site to improve the user experience and flow.
Responsive, desktop and mobile friendly.

www.brightwaygaragedoors.example

Main pages to be templated:

Homepage
Category pages/list e.g. https://www.brightwaygaragedoors.example/garage-doors/
Basic content/product pages e.g https://www.brightwaygaragedoors.example/veltrix-internal-doors/
Main services pages e.g. https://www.brightwaygaragedoors.example/garage-door-installation/
Branch pages e.g. https://www.brightwaygaragedoors.example/sidcup/
Contact page
-----------------------
Our logo must stay as is (the attached AI file has 3 elements - logo -BRIGHTWAY GARAGE DOORS with the 'B'mark, the SINCE 1976 mark and a tagline 'Far beyond your everyday garage doors' - these elements are to be used separately, not as a single block - although they can be combined)). Please use the text that’s already on the site in your design previews.
Our main colours are Blue RGB 35,57,119 and Red RGB 228,25,34

We would welcome a new smarter colour scheme but you will have to stick with the 2 primary colours we use on our logo - so any complimentary colours that might fit the new design would be great.

You can use all images that are on the website to support the new design - also attached is a zip with logo and images)

Target Market(s)

Most of our customers are in and around London - homeowners with garages that need servicing, replacing garage doors, upgrading or fitting new + other hiome improvements we can offer as listed above (fornt doors, bifold, sliding patio doors and awning) B2C

Industry/Entity Type

Home Improvement

Coding

Coded - Design and coding required

Font styles to use
Sans Serif

Requirements
Must have
• Custom and responsive design, user friendly, use our main 2 colours (red and blue described above) but add some complimentary colours to the mix
Nice to have
• Be creative, innovative
Should not have
• This should not be just some freely available wordpress template

```html
<!DOCTYPE html>
<html lang="en">
<head>
<meta charset="utf-8">
<title>Brightway Garage Doors – Home</title>
<link href="https://fonts.googleapis.com/css2?family=Open+Sans:wght@400;600;700&family=Raleway:wght@300;400;600;700&display=swap" rel="stylesheet">
<style>
:root{
  --blue:#233977;
  --red:#e41922;
  --red-dark:#b8141b;
  --ink:#333;
  --muted:#777;
  --grey-band:#f0f0f0;
  --dark:#3c3f44;
  --white:#fff;
}
*{box-sizing:border-box;margin:0;padding:0}
html,body{width:1200px;height:3376px;overflow:hidden}
body{font-family:"Open Sans",Arial,sans-serif;color:var(--ink);background:var(--white);position:relative}
.abs{position:absolute}
a{color:inherit;text-decoration:none}

/* top bar */
.topbar{top:0;left:0;width:1200px;height:32px;background:var(--blue)}
.topbar .social{left:22px;top:9px;display:flex;gap:6px}
.topbar .social span{width:14px;height:14px;border-radius:50%;background:var(--red)}
.topbar .callback{right:30px;top:6px;background:var(--red);color:#fff;font-size:9px;font-weight:700;padding:5px 12px;border-radius:2px;letter-spacing:.5px}

/* header */
.header{top:32px;left:0;width:1200px;height:88px;background:#fff;box-shadow:0 1px 4px rgba(0,0,0,.08)}
.brand{left:28px;top:22px;display:flex;align-items:center;gap:8px}
.brand .mark{width:30px;height:30px;background:var(--red)}
.brand .name{font-family:"Raleway",sans-serif;font-weight:700;font-size:15px;color:var(--blue);line-height:1.1}
.brand .tag{font-size:8px;color:var(--muted);display:block;font-weight:400}
.nav{left:470px;top:36px;display:flex;gap:20px;font-size:9.5px;font-weight:700;color:var(--blue);letter-spacing:.3px;white-space:nowrap}
.nav a{white-space:nowrap}
.nav .active{color:var(--red);border-bottom:2px solid var(--red);padding-bottom:6px}

/* hero */
.hero{top:120px;left:0;width:1200px;height:580px;background:linear-gradient(120deg,#4a4d52 0%,#6b6e73 45%,#2e3034 100%)}
.hero h1{left:56px;top:70px;font-family:"Raleway",sans-serif;font-weight:400;font-size:60px;color:#fff}
.hero p{left:56px;top:150px;width:470px;font-family:"Raleway",sans-serif;font-size:26px;line-height:1.3;color:#fff}
.hero .btns{left:56px;top:322px;display:flex;gap:14px}
.btn-ghost{border:1px solid #fff;color:#fff;font-size:11px;padding:9px 18px;border-radius:20px;font-weight:600}
.hero .side{right:40px;top:120px;border-left:2px solid rgba(255,255,255,.6);padding-left:14px;font-size:10px;color:#fff;line-height:2.6}
.hero .scroll{left:0;top:512px;width:118px;height:38px;background:rgba(255,255,255,.25);color:#fff;font-size:10px;padding:12px 14px}

/* intro */
.intro{top:700px;left:0;width:1200px;height:348px;text-align:center}
.intro h2{position:absolute;top:80px;width:100%;font-family:"Raleway",sans-serif;font-weight:400;font-size:22px;color:var(--ink);letter-spacing:.5px}
.intro h2 b,.red{color:var(--red)}
.intro p{position:absolute;top:126px;left:380px;width:440px;font-size:11px;color:var(--muted);line-height:1.6}
.intro .btns{position:absolute;top:220px;left:0;width:100%;display:flex;justify-content:center;gap:20px}
.btn-red{background:var(--red);color:#fff;font-size:11px;font-weight:700;padding:12px 34px;border-radius:24px}
.btn-line{border:1px solid var(--blue);color:var(--blue);font-size:11px;font-weight:700;padding:11px 30px;border-radius:24px}

/* services */
.services-head{top:1048px;left:0;width:1200px;height:120px;background:var(--grey-band);text-align:center}
.services-head h2{margin-top:48px;font-family:"Raleway",sans-serif;font-weight:400;font-size:22px}
.tile{top:1168px;height:452px}
.tile.left{left:0;width:372px;background:linear-gradient(160deg,#3b3f4a,#6a6f7a)}
.tile.mid{left:372px;width:480px;background:linear-gradient(180deg,#8a98a8 0%,#8b6b58 60%,#5a4d44 100%)}
.tile.right{left:852px;width:348px;background:linear-gradient(160deg,#8c8f94,#b5b7bb)}
.tile-label{left:386px;top:1434px;width:240px;padding:14px 18px;background:rgba(0,0,0,.45);border-left:4px solid var(--red);color:#fff;font-family:"Raleway",sans-serif;font-size:28px;line-height:1.1}
.arrow{width:24px;height:24px;border-radius:50%;background:rgba(255,255,255,.8)}

/* about */
.about h2{left:252px;top:1692px;font-family:"Raleway",sans-serif;font-weight:400;font-size:20px}
.about p{left:252px;top:1730px;width:320px;font-size:10px;line-height:1.6;color:var(--muted)}
.about ul{left:252px;top:1816px;list-style:none;font-size:10px;line-height:2}
.about li::before{content:"";display:inline-block;width:6px;height:6px;border-radius:50%;background:var(--red);margin-right:8px}
.video{left:600px;top:1690px;width:250px;height:170px;background:linear-gradient(150deg,#5c5247,#2f2b28)}

/* stats */
.stats{top:1920px;left:0;width:1200px;height:320px;background:linear-gradient(180deg,var(--red),var(--red-dark))}
.stat{top:2048px;width:160px;text-align:center;color:#fff}
.stat b{display:block;font-family:"Raleway",sans-serif;font-size:44px;font-weight:400}
.stat span{font-size:9px;font-weight:700;letter-spacing:.5px}

/* testimonials */
.card{top:2270px;width:240px;height:100px;background:#fff;box-shadow:0 2px 10px rgba(0,0,0,.1);padding:14px;font-size:10px;color:var(--muted);line-height:1.6}
.person{top:2400px;width:240px;text-align:center;font-size:9px}
.person i{display:block;margin:0 auto 6px;width:40px;height:40px;border-radius:50%;background:#c9b8a8}
.person small{display:block;color:var(--muted);font-size:8px}
.dots{top:2508px;left:576px;display:flex;gap:6px}
.dots span{width:6px;height:6px;border-radius:50%;background:#ccc}
.dots span:first-child{background:var(--red)}

/* callback form */
.callback-band{top:2580px;left:0;width:1200px;height:260px;background:var(--dark)}
.callback-title{left:250px;top:2684px;font-family:"Raleway",sans-serif;font-weight:400;font-size:20px;color:#fff}
.callback-text{left:250px;top:2716px;width:280px;font-size:9px;color:#bbb;line-height:1.5}
.field{height:24px;background:#fff;font-size:9px;color:#999;padding:6px 8px}
.submit{left:600px;top:2796px;width:340px;height:24px;background:var(--red);color:#fff;font-size:10px;font-weight:700;text-align:center;padding-top:5px}

/* partners */
.badge{top:2920px;height:56px;background:#d8d8d8;border-radius:4px}

/* footer */
.footer{top:3060px;left:0;width:1200px;height:280px;background:linear-gradient(180deg,var(--red),var(--red-dark))}
.footer-brand{left:270px;top:3120px;display:flex;align-items:center;gap:8px;color:#fff}
.footer-brand .mark{width:24px;height:24px;background:#fff}
.footer-brand .name{font-family:"Raleway",sans-serif;font-weight:700;font-size:12px;line-height:1.15}
.fcol{color:#fff;font-size:10px;line-height:1.9}
.fcol h4{font-size:12px;font-weight:700;margin-bottom:4px}
.fcol.note{font-size:9px;line-height:1.6}
.fcol .social{display:flex;gap:8px;margin-top:4px}
.fcol .social span{width:22px;height:22px;border-radius:50%;background:#fff}
.shot{left:800px;top:3186px;width:150px;height:90px;background:linear-gradient(150deg,#6b6e72,#3a3c40)}
.bottom{top:3340px;left:0;width:1200px;height:36px;background:var(--red-dark);color:#f5c4c6;font-size:8px;padding:14px 250px}
</style>
</head>
<body>

<div class="abs topbar">
  <div class="abs social"><span></span><span></span><span></span><span></span></div>
  <a class="abs callback">REQUEST A CALL BACK</a>
</div>

<header class="abs header">
  <div class="abs brand"><span class="mark"></span><span class="name">BRIGHTWAY GARAGE DOORS<span class="tag">Far beyond your everyday garage doors</span></span></div>
  <nav class="abs nav">
    <a class="active">HOME</a><a>OUR PRODUCTS ▾</a><a>INSTALLATION</a><a>REPAIRS</a><a>SPECIAL OFFERS</a><a>TESTIMONIALS</a><a>CONTACT US ▾</a><a>CAREERS</a>
  </nav>
</header>

<section class="abs hero" role="img" aria-label="Dining room with open bifold doors to the garden">
  <h1 class="abs">Bifold Doors</h1>
  <p class="abs">We pride ourselves on 100% satisfaction guaranteed by putting your needs and budget first.</p>
  <div class="abs btns"><a class="btn-ghost">View Garage Door Types</a><a class="btn-ghost">Get In Touch</a></div>
  <div class="abs side">Garage Door Types<br>Bifold Doors<br>Entrance Door Types</div>
  <div class="abs scroll">About Scrolling</div>
</section>

<section class="abs intro">
  <h2>UNRIVALLED SERVICE AT AFFORDABLE <b>PRICES</b></h2>
  <p>Brightway Garage Doors have been a trusted name in home improvements since 1976. Visit one of our five London showrooms to see our full range of doors and shading systems.</p>
  <div class="btns"><a class="btn-red">FIND A SHOWROOM</a><a class="btn-line">REQUEST A CALL BACK</a></div>
</section>

<section class="abs services-head"><h2>SOME OF OUR <span class="red">SERVICES</span></h2></section>
<div class="abs tile left" role="img" aria-label="Grey roller garage door"></div>
<div class="abs tile mid" role="img" aria-label="Brick house with a new garage door"></div>
<div class="abs tile right" role="img" aria-label="Close-up of a sectional garage door"></div>
<div class="abs tile-label">GARAG DOOR<br>TYPES</div>
<span class="abs arrow" style="left:20px;top:1380px"></span>
<span class="abs arrow" style="left:1156px;top:1380px"></span>

<section class="about">
  <h2 class="abs">BRIGHTWAY GARAGE <span class="red">DOORS</span></h2>
  <p class="abs">We are a garage door specialist providing installation, automation and repair services throughout South East England, with five branches across London and over 65 employees ready to help with your project.</p>
  <ul class="abs"><li>Friendly expert advice</li><li>FREE Estimates</li><li>Fully trained installers</li><li>Workmanship guaranteed</li><li>Affordable prices</li></ul>
  <div class="abs video" role="img" aria-label="Video still of a house with a garage door">
    <svg width="250" height="170" viewBox="0 0 250 170"><circle cx="125" cy="85" r="20" fill="rgba(255,255,255,.8)"/><path d="M119 75 L135 85 L119 95Z" fill="#e41922"/></svg>
  </div>
</section>

<section class="abs stats" aria-label="Company figures"></section>
<div class="abs stat" style="left:248px"><b>1850</b><span>PROJECTS</span></div>
<div class="abs stat" style="left:432px"><b>750</b><span>CLIENTS</span></div>
<div class="abs stat" style="left:608px"><b>2500</b><span>WORKERS</span></div>
<div class="abs stat" style="left:780px"><b>1700</b><span>COMPLETE PROJECTS</span></div>

<div class="abs card" style="left:264px">Great service from start to finish. The team fitted our new door quickly and left everything clean and tidy.</div>
<div class="abs card" style="left:572px">Friendly advice, a fair price and a lovely new front door. We would happily recommend them to anyone.</div>
<div class="abs card" style="left:872px">Our old garage door was repaired the same day. Very professional and helpful engineers throughout.</div>
<div class="abs person" style="left:264px"><i role="img" aria-label="Customer portrait"></i>Mark Ellison<small>Bexley, Kent</small></div>
<div class="abs person" style="left:572px"><i role="img" aria-label="Customer portrait"></i>Sarah Lowe<small>Sidcup, London</small></div>
<div class="abs person" style="left:872px"><i role="img" aria-label="Customer portrait"></i>David Okoro<small>Croydon, London</small></div>
<div class="abs dots"><span></span><span></span><span></span></div>

<section class="abs callback-band"></section>
<h2 class="abs callback-title">REQUEST A <span class="red">CALL BACK</span></h2>
<p class="abs callback-text">Our experts or a special offer team will be glad to call you back at a time that suits you.</p>
<div class="abs field" style="left:600px;top:2636px;width:166px">First Name</div>
<div class="abs field" style="left:774px;top:2636px;width:166px">Last Name</div>
<div class="abs field" style="left:600px;top:2668px;width:166px">Email</div>
<div class="abs field" style="left:774px;top:2668px;width:166px">Phone</div>
<div class="abs field" style="left:600px;top:2700px;width:340px;height:84px">Message</div>
<div class="abs submit">Submit</div>

<div class="abs badge" style="left:250px;width:110px" role="img" aria-label="Partner badge"></div>
<div class="abs badge" style="left:430px;width:80px" role="img" aria-label="Partner badge"></div>
<div class="abs badge" style="left:610px;width:90px" role="img" aria-label="Partner badge"></div>
<div class="abs badge" style="left:800px;width:110px" role="img" aria-label="Partner badge"></div>

<footer class="abs footer"></footer>
<div class="abs footer-brand"><span class="mark"></span><span class="name">BRIGHTWAY<br>GARAGE DOORS</span></div>
<div class="abs fcol" style="left:460px;top:3120px;width:90px"><h4>Get Started</h4>Home<br>Products<br>Installation<br>Repairs<br>Special Offers<br>Contact Us</div>
<div class="abs fcol note" style="left:570px;top:3150px;width:190px">Serving homeowners across London and South East England with garage doors, entrance doors and awnings since 1976.</div>
<div class="abs fcol" style="left:800px;top:3120px;width:200px"><h4>Follow Us</h4><div class="social"><span></span><span></span><span></span><span></span><span></span></div></div>
<div class="abs shot" role="img" aria-label="Showroom photo"></div>
<div class="abs bottom">© Brightway Garage Doors. All rights reserved.</div>

</body>
</html>
```